Vantor Business Card

I need a Business for my New Gym/Facility. I am the owner of Vantor Sports and Fitness. I would like my colors to be RED and Black. I will upload the LOGO design. I would like the card to say the following:Dennis T. Hale- Owner/CoachAddress: 2817 Willowgate Commerce Dr. Suite 304 Millbrook, OR 20151Tel: 541-378-4200rmack@optimumsnf.com

Industry/Entity Type

Fitness

Contact Information for Business Card

Very professional like a CEO's Card of a fortune 500 company look.

Font styles to use
Sans Serif

Requirements
Nice to have
• You can play with it be creative but extremely professional.
Should not have
• People on the card. No Bodies

```html
<!DOCTYPE html>
<html lang="en">
<head>
<meta charset="utf-8">
<title>Vantor Business Card</title>
<link rel="stylesheet" href="https://fonts.googleapis.com/css2?family=Jost:wght@400;500&display=swap">
<style>
  :root {
    --brand-red: #ec1f27;
    --ink: #3a3a3a;
    --muted: #6b6b6b;
    --rule: #9a9a9a;
    --paper: #ffffff;
    --backdrop: #e4e4e4;
  }
  * { margin: 0; padding: 0; box-sizing: border-box; }
  html, body {
    width: 1125px;
    height: 1200px;
    overflow: hidden;
    background: var(--backdrop);
    font-family: "Jost", sans-serif;
  }
  .canvas { position: relative; width: 1125px; height: 1200px; }

  .card {
    position: absolute;
    left: 150px;
    width: 826px;
    height: 470px;
    border-radius: 22px;
    overflow: hidden;
  }
  .card--front { top: 100px; background: var(--paper); }
  .card--front::before {
    content: "";
    position: absolute;
    left: 0; right: 0; bottom: 9px;
    height: 2px;
    background: var(--ink);
  }
  .card--front::after {
    content: "";
    position: absolute;
    left: 0; right: 0; bottom: 0;
    height: 9px;
    background: var(--brand-red);
  }
  .card--back { top: 632px; background: var(--brand-red); }

  .brand {
    position: absolute;
    top: 45px;
    left: 428px;
    display: flex;
    align-items: center;
    gap: 16px;
  }
  .brand__dot {
    width: 98px; height: 98px;
    border-radius: 50%;
    background: var(--brand-red);
    flex: none;
  }
  .brand__name {
    color: var(--brand-red);
    font-weight: 400;
    font-size: 30px;
    letter-spacing: 1px;
    text-transform: uppercase;
    line-height: 1.1;
  }

  .holder { position: absolute; left: 39px; top: 282px; }
  .holder__name {
    color: var(--brand-red);
    font-weight: 500;
    font-size: 31px;
    line-height: 1.1;
    text-transform: uppercase;
  }
  .holder__role {
    color: var(--ink);
    font-size: 21px;
    font-weight: 400;
    line-height: 1.3;
    text-transform: uppercase;
  }

  .divider {
    position: absolute;
    left: 39px; right: 44px; top: 360px;
    height: 1px;
    background: var(--rule);
  }

  .contact {
    position: absolute;
    left: 39px; top: 378px;
    list-style: none;
    color: var(--ink);
    font-size: 19px;
    line-height: 26px;
  }
  .contact li { display: flex; align-items: center; gap: 10px; }
  .contact svg { width: 17px; height: 17px; fill: var(--brand-red); }

  .address {
    position: absolute;
    right: 42px; top: 378px;
    text-align: right;
    color: var(--muted);
    font-size: 19px;
    line-height: 26px;
    font-style: normal;
  }

  .back-mark {
    position: absolute;
    left: 289px; top: 95px;
    width: 244px; height: 244px;
    border-radius: 50%;
    background: var(--paper);
    display: flex;
    align-items: center;
    justify-content: center;
  }
  .back-mark__name {
    color: var(--brand-red);
    font-size: 34px;
    font-weight: 500;
    letter-spacing: 3px;
    text-transform: uppercase;
  }
  .website {
    position: absolute;
    left: 0; right: 0; top: 388px;
    text-align: center;
    color: var(--paper);
    font-size: 19px;
    font-weight: 500;
    letter-spacing: 4px;
    text-transform: uppercase;
  }
</style>
</head>
<body>
<main class="canvas">
  <section class="card card--front">
    <div class="brand">
      <span class="brand__dot"></span>
      <span class="brand__name">Vantor Sports<br>and Fitness</span>
    </div>

    <div class="holder">
      <h1 class="holder__name">Dennis T. Hale</h1>
      <p class="holder__role">Owner/Coach</p>
    </div>

    <div class="divider"></div>

    <ul class="contact">
      <li>
        <svg viewBox="0 0 24 24" aria-hidden="true"><path d="M6.6 10.8a15.1 15.1 0 0 0 6.6 6.6l2.2-2.2c.3-.3.7-.4 1-.2 1.1.4 2.3.6 3.6.6.6 0 1 .4 1 1V20c0 .6-.4 1-1 1A17 17 0 0 1 3 4c0-.6.4-1 1-1h3.5c.6 0 1 .4 1 1 0 1.3.2 2.5.6 3.6.1.3 0 .7-.2 1z"/></svg>
        541-555-0192
      </li>
      <li>
        <svg viewBox="0 0 24 24" aria-hidden="true"><path d="M2 5h20v14H2z M2 5l10 8 10-8" /></svg>
        dhale@vantorspf.example
      </li>
    </ul>

    <address class="address">
      2817 Willowgate Commerce Dr.<br>
      Suite 304 Millbrook, OR 20468
    </address>
  </section>

  <section class="card card--back">
    <div class="back-mark">
      <span class="back-mark__name">Vantor</span>
    </div>
    <p class="website">www.vantorspf.example</p>
  </section>
</main>
</body>
</html>
```